Property developer, money partner needs business card design using logo concept provided

Our company develops residential properties, does money lends for joint ventures in property deals and finds property deals for other money partners. We have provided a basic logo for you to work from. Any graphic or logo design on the card is to communicate development and finance collaboration. Color choice is not so important for us, but color choice does need to reflect professionalism.

```html
<!DOCTYPE html>
<html lang="en">
<head>
<meta charset="utf-8">
<title>Brightvale Property Solutions – Business Card</title>
<link href="https://fonts.googleapis.com/css2?family=Montserrat:wght@400;500;700&family=Open+Sans:wght@400&display=swap" rel="stylesheet">
<style>
  :root {
    --backdrop: #3b3b3d;
    --card-white: #ffffff;
    --card-white-shade: #f2f2f4;
    --card-black: #161616;
    --card-black-shade: #222224;
    --ink: #1c1c1c;
    --ink-soft: #444;
    --brand-blue: #1565b8;
    --brand-blue-deep: #0a4c9a;
    --brand-blue-light: #1e88d0;
    --rule: #9a9a9a;
    --white: #ffffff;
  }
  * { box-sizing: border-box; margin: 0; padding: 0; }
  html, body { width: 1200px; height: 1200px; overflow: hidden; }
  body {
    background: var(--backdrop);
    font-family: "Montserrat", sans-serif;
    display: flex;
    flex-direction: column;
    align-items: center;
    justify-content: center;
    gap: 44px;
  }
  .card {
    position: relative;
    width: 920px;
    height: 520px;
    border-radius: 34px;
    overflow: hidden;
    box-shadow: 0 16px 36px rgba(0,0,0,.45);
  }

  /* Front */
  .card-front {
    background: linear-gradient(180deg, var(--card-white) 60%, var(--card-white-shade) 100%);
  }
  .front-band {
    position: absolute; left: 0; right: 0; bottom: 0; height: 22px;
    background: linear-gradient(90deg, var(--brand-blue-deep), var(--brand-blue-light) 55%, var(--brand-blue-deep));
  }
  .brand {
    position: absolute;
    display: flex;
    align-items: center;
    gap: 22px;
  }
  .brand-front { left: 190px; top: 120px; }
  .brand-mark {
    width: 96px; height: 96px; border-radius: 50%;
    background: linear-gradient(160deg, var(--brand-blue-light), var(--brand-blue-deep));
    flex: none;
  }
  .brand-text { color: var(--ink); font-family: "Montserrat", sans-serif; font-weight: 700; line-height: 1.15; }
  .brand-name { font-size: 40px; letter-spacing: 10px; }
  .brand-sub { font-size: 22px; letter-spacing: 7px; }
  .brand-acn { font-size: 14px; letter-spacing: 4px; margin-left: 110px; }

  .person {
    position: absolute; left: 110px; top: 318px;
    border-left: 7px solid var(--brand-blue);
    padding-left: 16px;
  }
  .person-name { font-size: 46px; font-weight: 500; color: var(--brand-blue); letter-spacing: -1px; line-height: 1; }
  .person-role { font-size: 24px; font-weight: 400; color: var(--ink-soft); margin-top: 4px; }

  .divider {
    position: absolute; left: 468px; top: 290px; width: 1px; height: 140px;
    background: var(--rule);
  }
  .contacts {
    position: absolute; left: 510px; top: 300px;
    list-style: none;
    font-family: "Open Sans", sans-serif;
    color: var(--ink-soft);
    font-size: 26px;
  }
  .contacts li { display: flex; align-items: center; gap: 14px; height: 40px; }
  .contacts svg { width: 26px; height: 26px; flex: none; }

  /* Back */
  .card-back {
    background: linear-gradient(180deg, var(--card-black-shade), var(--card-black));
    display: flex; align-items: center; justify-content: center;
  }
  .card-back .brand { position: static; flex-direction: column; gap: 34px; }
  .card-back .brand-mark { width: 170px; height: 170px; }
  .card-back .brand-text { color: var(--white); text-align: center; }
  .card-back .brand-name { font-size: 50px; }
  .card-back .brand-sub { font-size: 26px; }
  .card-back .brand-acn { margin-left: 0; font-size: 16px; }
</style>
</head>
<body>

<section class="card card-front" aria-label="Business card front">
  <div class="brand brand-front">
    <div class="brand-text">
      <div class="brand-name">BRIGHTVALE</div>
      <div class="brand-sub">Property Solutions</div>
      <div class="brand-acn">A.C.N 418 093 256</div>
    </div>
    <div class="brand-mark"></div>
  </div>

  <div class="person">
    <div class="person-name">FULL NAME</div>
    <div class="person-role">POSITION</div>
  </div>

  <div class="divider"></div>

  <ul class="contacts">
    <li>
      <svg viewBox="0 0 24 24" aria-hidden="true"><path fill="#1565b8" d="M6.6 10.8a15 15 0 0 0 6.6 6.6l2.2-2.2c.3-.3.7-.4 1-.2 1.1.4 2.3.6 3.6.6.6 0 1 .4 1 1V20c0 .6-.4 1-1 1A17 17 0 0 1 3 4c0-.6.4-1 1-1h3.5c.6 0 1 .4 1 1 0 1.3.2 2.5.6 3.6.1.3 0 .7-.2 1z"/></svg>
      (000) 000 0000
    </li>
    <li>
      <svg viewBox="0 0 24 24" aria-hidden="true"><rect x="2" y="5" width="20" height="14" fill="#1565b8"/><path d="M2 5l10 8 10-8" fill="none" stroke="#fff" stroke-width="1.6"/></svg>
      email@company.com
    </li>
    <li>
      <svg viewBox="0 0 24 24" aria-hidden="true"><circle cx="12" cy="12" r="10" fill="#1565b8"/><g fill="none" stroke="#fff" stroke-width="1.2"><ellipse cx="12" cy="12" rx="4.5" ry="10"/><path d="M2 12h20M4 7h16M4 17h16M12 2v20"/></g></svg>
      www.company.com
    </li>
  </ul>

  <div class="front-band"></div>
</section>

<section class="card card-back" aria-label="Business card back">
  <div class="brand">
    <div class="brand-mark"></div>
    <div class="brand-text">
      <div class="brand-name">BRIGHTVALE</div>
      <div class="brand-sub">Property Solutions</div>
      <div class="brand-acn">A.C.N 418 093 256</div>
    </div>
  </div>
</section>

</body>
</html>
```